Become a Mentor - For Musicians, Artists, Producers and Teachers

Here is the full creative brief:

https://sheets.quarnelpad.com/file/d/7kTmRwQpZ_3LcN8bJ2HsX5vD4FnYgA9eWu0iPoKqtrr/view?mode=shared

Here is the background image file: https://www.vellicrate.com/sh/48tbnwqzd7kpm3f/AAJx2h8QPW5LuTkZZ-bn4RXCo?dl=0

LOGO:
https://www.vellicrate.com/sh/k273mrtjuz6c8w1/AAHLQ5PrTB9Y-vNJZcKsWp0Ue?dl=0

```html
<!DOCTYPE html>
<html lang="en">
<head>
<meta charset="utf-8">
<title>Become a Mentor – Meridian School of Music</title>
<link rel="stylesheet" href="https://fonts.googleapis.com/css2?family=Alegreya+Sans+SC:wght@800&family=Roboto:ital,wght@0,400;1,300&family=Josefin+Sans:wght@600;700&display=swap">
<style>
  :root {
    --page: #ffffff;
    --ink: #141113;
    --accent: #f04a3f;
    --white: #ffffff;
    --muted: #c4c0c1;
    --red-light: #b4443b;
    --red-mid: #7a2a25;
    --red-deep: #2e1210;
    --grey-light: #5e5a5b;
    --grey-mid: #38383a;
    --grey-deep: #161415;
  }
  * { margin: 0; padding: 0; box-sizing: border-box; }
  html, body { width: 1200px; height: 1000px; overflow: hidden; background: var(--page); }
  .poster {
    position: absolute; left: 281px; top: 48px;
    width: 637px; height: 905px;
    background: var(--ink); overflow: hidden;
    font-family: "Roboto", Arial, sans-serif; color: var(--white);
  }
  .poster-art { position: absolute; inset: 0; width: 637px; height: 905px; }
  .brand {
    position: absolute; left: 440px; top: 38px; width: 190px;
    text-align: center; font-family: "Josefin Sans", Arial, sans-serif;
    font-weight: 600; font-size: 15px; line-height: 18px; letter-spacing: 1px;
    color: var(--white); text-transform: uppercase;
  }
  .kicker {
    position: absolute; left: 42px; top: 451px;
    font-style: italic; font-weight: 300; font-size: 23px; color: var(--muted);
  }
  .headline {
    position: absolute; left: 43px; top: 504px;
    font-family: "Alegreya Sans SC", "Arial Black", sans-serif; font-weight: 800;
    font-size: 58px; line-height: 54px; letter-spacing: 2px; text-transform: uppercase;
  }
  .lede {
    position: absolute; left: 44px; top: 678px;
    font-size: 20px; line-height: 32px; letter-spacing: 0.6px;
  }
  .divider { position: absolute; left: 43px; top: 754px; width: 294px; height: 8px; }
  .cta {
    position: absolute; left: 45px; top: 784px;
    display: flex; align-items: center; gap: 16px;
    font-family: "Josefin Sans", Arial, sans-serif; font-weight: 600;
    font-size: 27px; letter-spacing: 2px; text-transform: uppercase;
  }
  .cta-phone { display: flex; align-items: center; gap: 10px; font-weight: 700; font-size: 30px; letter-spacing: 2px; }
  .web-bar {
    position: absolute; left: 0; top: 849px; width: 436px; height: 56px;
    background: var(--accent); display: flex; align-items: center; gap: 12px;
    padding-left: 44px; font-size: 20px; letter-spacing: 0.3px;
  }
</style>
</head>
<body>
<main class="poster">
  <svg class="poster-art" viewBox="0 0 637 905">
    <defs>
      <radialGradient id="photoRed" cx="0.25" cy="0.45" r="0.9">
        <stop offset="0" stop-color="var(--red-light)"/>
        <stop offset="0.45" stop-color="var(--red-mid)"/>
        <stop offset="1" stop-color="var(--red-deep)"/>
      </radialGradient>
      <radialGradient id="photoGrey" cx="0.55" cy="0.3" r="0.9">
        <stop offset="0" stop-color="var(--grey-light)"/>
        <stop offset="0.5" stop-color="var(--grey-mid)"/>
        <stop offset="1" stop-color="var(--grey-deep)"/>
      </radialGradient>
    </defs>
    <rect class="studio-photo" x="0" y="0" width="637" height="500" fill="url(#photoRed)" role="img" aria-label="Photo with red tint: two producers talking at a studio mixing desk"/>
    <path class="accent-wedge" d="M0,388 L70,350 L0,418 Z" fill="var(--accent)"/>
    <path class="content-field" d="M0,442 L150,338 Q185,318 215,328 Q238,338 246,365 L258,420 L560,684 L637,684 L637,905 L0,905 Z" fill="var(--ink)"/>
    <path class="studio-photo-panel" d="M262,444 Q250,428 262,414 L530,128 Q548,108 575,104 L637,104 L637,666 L590,666 Q575,666 563,658 L292,482 Q266,466 262,444 Z" fill="url(#photoGrey)" role="img" aria-label="Photo: close view of hands over a studio mixing console with a monitor speaker"/>
    <path class="accent-rule" d="M257,428 Q255,468 286,489 L558,670 Q572,678 592,678 L637,678" fill="none" stroke="var(--accent)" stroke-width="4"/>
    <path class="brand-block" d="M419,0 L637,0 L637,102 L465,102 Q419,102 419,56 Z" fill="var(--ink)"/>
  </svg>

  <div class="brand">Meridian<br>School of Music</div>

  <p class="kicker">Start your career</p>
  <h1 class="headline">Become<br>a Mentor<br>Today</h1>
  <p class="lede">Turn your skills and passion for music into a career<br>Designed for Musicians, Artists, Producers &amp; Teachers</p>

  <svg class="divider" viewBox="0 0 294 8" aria-hidden="true">
    <circle cx="4" cy="4" r="3.5" fill="var(--white)"/>
    <rect x="4" y="3" width="290" height="2" fill="var(--white)"/>
  </svg>

  <div class="cta">
    <span>Apply now</span>
    <span class="cta-phone">
      <svg width="26" height="36" viewBox="0 0 26 36" aria-hidden="true">
        <path d="M8,2 L13,11 Q13,14 9,15 Q9,20 13,25 Q16,24 18,25 L23,33 Q21,35 17,35 Q6,33 3,18 Q2,6 8,2 Z" fill="var(--white)"/>
      </svg>
      1300 482 482
    </span>
  </div>

  <div class="web-bar">
    <svg width="20" height="20" viewBox="0 0 20 20" aria-hidden="true">
      <circle cx="10" cy="10" r="9" fill="var(--white)"/>
      <path d="M5,5 Q9,6 8,10 Q6,12 7,16 L9,16 Q10,12 9,9 Z M12,3 Q11,7 14,8 Q16,10 15,13 L17,11 Q17,6 12,3 Z" fill="var(--accent)"/>
    </svg>
    <span>www.meridianschoolofmusic.com.au</span>
  </div>
</main>
</body>
</html>
```